small business focused on life coaching and helping others "create better tomorrows" needs a website

The Pax T Group needs a website that focuses on life coaching and helping others "create better tomorrows"; This is a sole proprietorship so the focus should be on Marla, who has worn many hats and in an excellent position to help others. It should include 6 pages _ Home, Bio, Services, Book, Media, Contact Us and the logo that was created by Lumo Forge; also include testimonials from 5-6 individuals as well as why one might need these services (see file included)

Target Market(s)

Immigrants who need help navigating American system in the workplace, home or community, immigrant or at-risk students unable to communicate with their immigrant parents (due to language or unfamiliarity with the new culture) but would share with someone they trust, those in need of a mentor or help with career advancement or choices, those in need of help with public speaking or leadership development - Marla is someone who has worn many hats and in a position to help - extensive networking, an immigrant herself, former teacher, community leader, TV talk show host, author, mother, grandmother, etc.

Industry/Entity Type

Business

Coding

Coded - Design and coding required

Number of Pages Required

5+ page

Font styles to use
Sans Serif

Colors
cadf82
add136

Requirements
Must have
• visuals of Marla - present image of competency, caring, professionalism; need to include a 30-second video (in process of being produced) of Marla promoting the services, need to include 5-6 testimonials (which will be sent later). Please see the document that describes the different pages of the website and what should be included. Give the image of Marla's ability to help people GROW into a more productive self
Nice to have
• This is a sole proprietor business and as such, need to have people feel comfortable in who I am - trust is critical and that is why experience and competency should be shown

```html
<!DOCTYPE html>
<html lang="en">
<head>
<meta charset="utf-8">
<title>The Pax T Group — Life Coaching</title>
<link href="https://fonts.googleapis.com/css2?family=Open+Sans:wght@300;400;600;700&display=swap" rel="stylesheet">
<style>
:root{
  --green:#add136;
  --green-soft:#cadf82;
  --green-dark:#8fb22a;
  --ink:#333;
  --muted:#777;
  --light:#f1f1f1;
  --footer:#3b3b3b;
  --footer-deep:#2c2c2c;
  --white:#fff;
  --red:#d62a2a;
}
*{box-sizing:border-box;margin:0;padding:0}
html,body{width:1200px;height:2756px;overflow:hidden}
body{font-family:"Open Sans",Arial,sans-serif;color:var(--ink);background:var(--white);font-size:13px;line-height:1.6}
.site-header{height:112px;display:flex;align-items:center;justify-content:space-between;padding:0 40px}
.brand{display:flex;align-items:center;gap:10px;font-weight:600;font-size:19px;color:var(--ink)}
.brand-square{width:14px;height:14px;background:var(--green)}
.main-nav{display:flex}
.main-nav a{font-size:12px;font-weight:600;color:var(--ink);text-decoration:none;padding:10px 16px;letter-spacing:.5px}
.main-nav a.active{color:var(--green-dark);border-bottom:2px solid var(--green)}
.hero{position:relative;height:648px;background:linear-gradient(135deg,#c9c3b8 0%,#8d8378 40%,#5a524c 70%,#9b958c 100%)}
.hero-banner{position:absolute;right:0;top:420px;width:560px;height:124px;background:linear-gradient(90deg,rgba(173,209,54,0),rgba(173,209,54,.85) 25%,rgba(143,178,42,.95));color:var(--white);font-size:36px;font-weight:300;line-height:1.2;padding:14px 0 0 140px}
.hero-banner span{display:block;padding-left:90px}
.welcome{height:296px;padding:44px 100px 0;display:flex;gap:50px}
.welcome-text{flex:1}
.section-title{font-size:28px;font-weight:300;color:var(--green-dark);margin-bottom:18px}
.welcome-text p{color:var(--muted);font-size:12px;margin-bottom:14px}
.video-thumb{position:relative;width:240px;height:240px;border-radius:50%;background:linear-gradient(160deg,#d8d2ca,#7a6f66);flex:none;margin-top:-10px;border:4px solid var(--white);box-shadow:0 2px 8px rgba(0,0,0,.2)}
.play{position:absolute;left:88px;top:96px;width:56px;height:40px;border-radius:10px;background:var(--red)}
.special{height:560px;background:var(--light);padding:44px 80px 0;text-align:center;position:relative}
.special .section-title{font-size:34px;margin-bottom:6px}
.sub{color:var(--muted);font-size:11px;margin-bottom:30px}
.cards{display:flex;gap:22px;text-align:left}
.card{flex:1}
.card-photo{height:170px;margin-bottom:14px}
.card h3{font-size:15px;font-weight:600;color:var(--green-dark);line-height:1.3;margin-bottom:8px}
.card p{font-size:11px;color:var(--muted)}
.arrow{position:absolute;top:300px;width:28px;height:28px}
.arrow.left{left:30px}.arrow.right{right:30px}
.better{height:440px;display:flex;background:var(--green)}
.better-photo{width:540px;background:linear-gradient(135deg,#b9a58f,#6d5d52 50%,#a89a8a)}
.better-copy{flex:1;padding:36px 50px;color:var(--white)}
.better-copy h2{font-size:32px;font-weight:300;margin-bottom:18px}
.checklist{list-style:none}
.checklist li{display:flex;gap:10px;align-items:flex-start;font-size:12px;margin-bottom:11px;border-bottom:1px solid rgba(255,255,255,.35);padding-bottom:8px}
.checklist svg{flex:none;margin-top:3px}
.testimonials{height:464px;padding:50px 100px 0;text-align:center}
.testimonials .section-title{font-size:34px;margin-bottom:6px}
.quotes{display:flex;gap:40px;text-align:left;margin-top:30px}
.quote{flex:1}
.quote-box{background:var(--light);padding:26px 30px;font-size:12px;color:var(--muted);font-style:italic;position:relative}
.quote-box::after{content:"";position:absolute;left:40px;bottom:-14px;border:14px solid transparent;border-bottom:0;border-top-color:var(--light)}
.quote-name{margin-top:26px;font-weight:700;color:var(--green-dark);font-size:13px}
.quote-date{font-size:11px;color:var(--muted)}
.site-footer{height:200px;background:var(--footer);color:#ccc;display:flex;padding:40px 80px 0;gap:50px}
.foot-brand{width:230px;display:flex;align-items:center;justify-content:center;gap:10px;height:60px;color:var(--white);font-size:18px;font-weight:600}
.foot-col{flex:1;font-size:11px}
.foot-col h4{color:var(--white);font-size:13px;font-weight:700;margin-bottom:12px;letter-spacing:1px}
.foot-col p{margin-bottom:5px}
.signup{display:flex;flex-direction:column;gap:8px;margin-top:8px}
.signup .field{height:26px;background:var(--white);width:190px}
.signup .btn{height:24px;width:80px;background:var(--green);color:var(--white);font-size:10px;font-weight:700;text-align:center;line-height:24px}
.socials{display:flex;gap:8px;margin-bottom:10px}
.socials span{width:26px;height:26px;border-radius:50%;border:1px solid #ccc}
.copyright{height:36px;background:var(--footer-deep);color:#aaa;font-size:10px;text-align:center;line-height:36px}
</style>
</head>
<body>
<header class="site-header">
  <div class="brand"><span class="brand-square"></span>The Pax T Group</div>
  <nav class="main-nav"><a class="active">HOME</a><a>BIO</a><a>SERVICES</a><a>BOOK</a><a>MEDIA</a><a>CONTACT US</a></nav>
</header>

<section class="hero" role="img" aria-label="Photo of Marla and a colleague at an office desk">
  <div class="hero-banner">Helping Create<span>Better Tomorrows</span></div>
</section>

<section class="welcome">
  <div class="welcome-text">
    <h1 class="section-title">Welcome to the Pax T Group</h1>
    <p>Hi, welcome to the Pax T Group, I'm Marla. When you're looking for someone to guide you through life's ups and downs, you need someone who has been there. I have walked many roads as an immigrant, a teacher, a community leader, a talk show host, an author, a mother and a grandmother, and each one taught me how to help people grow with patience and care.</p>
    <p>As an immigrant who has grown up in this country, I know how it feels to stand between two cultures. I have helped families, students and professionals find their voice at work, at home and in the community. Let me help you write your own story and create a better tomorrow, one step at a time.</p>
  </div>
  <div class="video-thumb" role="img" aria-label="Video preview of Marla introducing her services"><span class="play"></span></div>
</section>

<section class="special">
  <h2 class="section-title">Special Areas</h2>
  <p class="sub">Marla has helped immigrants navigate a system foreign to them and helped their children bridge cultural gaps</p>
  <svg class="arrow left" viewBox="0 0 28 28"><path d="M18 5 9 14l9 9" fill="none" stroke="#999" stroke-width="3"/></svg>
  <svg class="arrow right" viewBox="0 0 28 28"><path d="M10 5l9 9-9 9" fill="none" stroke="#999" stroke-width="3"/></svg>
  <div class="cards">
    <article class="card"><div class="card-photo" role="img" aria-label="Photo of Marla mentoring a client" style="background:linear-gradient(135deg,#c6b8a8,#7f6f63)"></div><h3>Careers</h3><p>Marla has helped immigrants navigate a system foreign to them and helped their children bridge gaps.</p></article>
    <article class="card"><div class="card-photo" role="img" aria-label="Photo of Marla with a family" style="background:linear-gradient(135deg,#b9b1a5,#6b625a)"></div><h3>Acculturation</h3><p>Marla has helped immigrants navigate a system foreign to them and helped their children bridge gaps.</p></article>
    <article class="card"><div class="card-photo" role="img" aria-label="Photo of Marla speaking at a podium" style="background:linear-gradient(135deg,#d2c5b6,#8c7b6c)"></div><h3>Leadership Development /<br>Public Speaking</h3><p>Marla has helped immigrants navigate a system foreign to them and helped their children bridge gaps.</p></article>
    <article class="card"><div class="card-photo" role="img" aria-label="Photo of Marla with students" style="background:linear-gradient(135deg,#c0b4a6,#75685d)"></div><h3>Inter-generational Solutions</h3><p>Marla has helped immigrants navigate a system foreign to them and helped their children bridge gaps.</p></article>
  </div>
</section>

<section class="better">
  <div class="better-photo" role="img" aria-label="Photo of Marla with two community leaders"></div>
  <div class="better-copy">
    <h2>Creating Better Tomorrows</h2>
    <ul class="checklist">
      <li><svg width="14" height="14" viewBox="0 0 14 14"><path d="M2 7l3 3 7-7" fill="none" stroke="#fff" stroke-width="2"/></svg>Are you an immigrant needing help navigating the American system?</li>
      <li><svg width="14" height="14" viewBox="0 0 14 14"><path d="M2 7l3 3 7-7" fill="none" stroke="#fff" stroke-width="2"/></svg>Are you an immigrant parent unable to connect with your children's school or culture?</li>
      <li><svg width="14" height="14" viewBox="0 0 14 14"><path d="M2 7l3 3 7-7" fill="none" stroke="#fff" stroke-width="2"/></svg>Do you need help with your career choices?</li>
      <li><svg width="14" height="14" viewBox="0 0 14 14"><path d="M2 7l3 3 7-7" fill="none" stroke="#fff" stroke-width="2"/></svg>Are you considering a career change?</li>
      <li><svg width="14" height="14" viewBox="0 0 14 14"><path d="M2 7l3 3 7-7" fill="none" stroke="#fff" stroke-width="2"/></svg>Are you struggling to balance demands at home, work and community?</li>
      <li><svg width="14" height="14" viewBox="0 0 14 14"><path d="M2 7l3 3 7-7" fill="none" stroke="#fff" stroke-width="2"/></svg>Do you need help with time management, leadership development?</li>
      <li><svg width="14" height="14" viewBox="0 0 14 14"><path d="M2 7l3 3 7-7" fill="none" stroke="#fff" stroke-width="2"/></svg>Are you nervous about your next talk in front of others?</li>
      <li><svg width="14" height="14" viewBox="0 0 14 14"><path d="M2 7l3 3 7-7" fill="none" stroke="#fff" stroke-width="2"/></svg>Is your family struggling with an intergenerational language gap?</li>
    </ul>
  </div>
</section>

<section class="testimonials">
  <h2 class="section-title">Our Testimonials</h2>
  <p class="sub">Marla has helped immigrants navigate a system foreign to them and helped their children bridge cultural gaps</p>
  <div class="quotes">
    <div class="quote">
      <div class="quote-box">"Marla is the real deal. She listened, guided and never judged. When I was lost in a new country and a new job, she helped me see a path forward and gave me the confidence to take it. My family and I are grateful for her warm support."</div>
      <div class="quote-name">DANA K</div><div class="quote-date">Posted on 06 Oct 2017</div>
    </div>
    <div class="quote">
      <div class="quote-box">"Thank you to Marla for helping me and my son talk again. She understood both of our worlds and found the words we could not. Her advice on public speaking also helped me land a new role. I recommend her to anyone who wants to grow."</div>
      <div class="quote-name">OMAR L</div><div class="quote-date">Posted on 06 Oct 2017</div>
    </div>
  </div>
</section>

<footer class="site-footer">
  <div class="foot-brand"><span class="brand-square"></span>The Pax T Group</div>
  <div class="foot-col">
    <h4>CONTACT US</h4>
    <p>(555) 014-2290 (Phone)</p>
    <p>(555) 014-2291 (Fax)</p>
    <p>hello@paxtgroup.example</p>
    <p>18 Orchard Lane,<br>Brookfield, ST 00000</p>
  </div>
  <div class="foot-col">
    <h4>NEWSLETTER</h4>
    <p>Register your email address to get information about us</p>
    <div class="signup"><span class="field"></span><span class="btn">SUBSCRIBE</span></div>
  </div>
  <div class="foot-col">
    <h4>FOLLOW US</h4>
    <div class="socials"><span></span><span></span><span></span><span></span><span></span><span></span></div>
    <p>Stay close for news, events and fresh ideas to help you create a better tomorrow.</p>
  </div>
</footer>
<div class="copyright">© Copyright 2017 The Pax T Group All Rights Reserved</div>
</body>
</html>
```